Electronic Music Artist needs an Album Cover

DRELL is an electronic musician from Boston, Massachusetts. He needs an album cover that captures the essence of his music. The album is called Lanterns, which represents his experiences growing up, positive and negative. He would like to see designs that involves color and creativity. Attached are some examples of artworks that DRELL likes. He also included a few of his original photos (optional to use. Using a photo will not effect his final decision!), and his logo.

Colors

Designer to choose colors to be used in the design.

Requirements
Must have
• My project must have the text "Lanterns" and "DRELL", and the logo (attached in the files). The logo should not be the main subject of the artwork. Everything must look aesthetically pleasing.
Nice to have
• It would be nice to have some sort of creative graphic design (see example album covers for reference). Also, in one of the references, there is a column on the left hand side with some text in it. That could be cool to include, but without the asian text.
Should not have
• The project should not have any other language besides English.

```html
<!DOCTYPE html>
<html lang="en">
<head>
<meta charset="utf-8">
<title>DRELL — Lanterns</title>
<link rel="stylesheet" href="https://fonts.googleapis.com/css2?family=Oswald:wght@300&display=swap">
<style>
  :root {
    --cover-red: #6b1b22;
    --title-cream: #f3ece4;
    --title-mint: #2fe08a;
    --art-navy: #1c1f4a;
    --art-green: #3f8f2a;
    --art-magenta: #7a1f4a;
    --art-ink: #0f1f22;
  }
  html, body {
    margin: 0;
    padding: 0;
    width: 1200px;
    height: 1200px;
    overflow: hidden;
    background: var(--cover-red);
  }
  .album-cover {
    position: relative;
    width: 1200px;
    height: 1200px;
    background: var(--cover-red);
    font-family: "Oswald", sans-serif;
  }
  .cover-title {
    position: absolute;
    top: 128px;
    left: 0;
    width: 1200px;
    margin: 0;
    text-align: center;
    font-weight: 300;
    font-size: 58px;
    line-height: 1;
    letter-spacing: 46px;
    text-indent: 46px;
    white-space: nowrap;
  }
  .artist-name { color: var(--title-cream); }
  .album-name { color: var(--title-mint); }
  .cover-artwork {
    position: absolute;
    left: 0;
    top: 216px;
    width: 1168px;
    height: 880px;
    border-radius: 46% 40% 44% 50% / 40% 46% 54% 50%;
    background:
      radial-gradient(ellipse 38% 30% at 30% 28%, rgba(63,143,42,0.85), transparent 70%),
      radial-gradient(ellipse 34% 28% at 62% 30%, rgba(63,143,42,0.8), transparent 70%),
      radial-gradient(ellipse 40% 40% at 50% 70%, var(--art-navy), transparent 75%),
      radial-gradient(ellipse 50% 50% at 50% 50%, var(--art-magenta), transparent 80%),
      radial-gradient(ellipse 60% 55% at 50% 50%, rgba(15,31,34,0.7), transparent 85%);
  }
  .artist-mark {
    position: absolute;
    right: 20px;
    bottom: 26px;
    width: 184px;
    text-align: center;
    color: var(--title-cream);
    font-weight: 300;
    font-size: 64px;
    line-height: 1;
    letter-spacing: 4px;
  }
</style>
</head>
<body>
  <main class="album-cover">
    <h1 class="cover-title"><span class="artist-name">DRELL</span> <span class="album-name">LANTERNS</span></h1>
    <div class="cover-artwork" role="img" aria-label="Abstract flowing artwork of layered waves and brush strokes in green, navy, magenta and dark teal"></div>
    <div class="artist-mark">DRELL</div>
  </main>
</body>
</html>
```